Ardo Move - A non profit for healthy lifestyle and fitness within refugee camps

We need a logo and website design for a new 501c3 Non-Profit based in San Francisco called 'Ardo Move'. We help coordinate trips across the globe to provide fitness classes to refugee camps to help refugees maintain a healthy lifestyle and fun while exercising.
Our first trip was to Greece and we hope to extend our reach by working with other non-profits to coordinate how we can help bring a healthy lifestyle and a wellness to refugees in need.
We would like to see website design that use the color green and blue. The final design should represent a welcoming website to encourage people to take a trip either by themselves, as a group, or with a corporate team.
We have 3 certified and experienced trainers that will be running these trips and with a hope of 20 volunteers per trip to help.

We are hoping to partner with another 501c3 called 'Tide of Hope' which I have participated in and with the hopes of providing an easier and simpler user experience than their current website but with many of the same content.

We would like a 'Trips' page with previous trips, 'Trainers/Hosts' page with bios of the leaders hosting the event, 'Register Page' for folks to register for upcoming trips, 'About Us' page for our mission statement and work, 'Albums' page for photos taken on the trip, 'Contact Us' page for FAQs and questions to submit, and a 'Donate' page for people to donate to our cause.

I would like this page to be created in Word Press.

ie: http://www.tideofhopeexample.com.au/programs/

Target Market(s)

Volunteers, non-profit partners

Industry/Entity Type

Non-Profit

Number of Pages Required

4 page

Font styles to use
Sans Serif

Colors

Designer to choose colors to be used in the design.

Requirements
Must have
• 'Trips' page with previous trips, 'Trainers/Hosts' page with bios of the leaders hosting the event, 'Register Page' for folks to register for upcoming trips, 'About Us' page for our mission statement and work, 'Albums' page for photos taken on the trip, 'Contact Us' page for FAQs and questions to submit, and a 'Donate' page for people to donate to our cause.

```html
<!DOCTYPE html>
<html lang="en">
<head>
<meta charset="utf-8">
<title>Ardo Move</title>
<link rel="stylesheet" href="https://fonts.googleapis.com/css2?family=Bree+Serif&family=Poppins:wght@300;400;500;600&family=Roboto:wght@400;500&display=swap">
<style>
:root{
  --teal:#14b99b;
  --teal-dark:#0f9e84;
  --ink:#222;
  --body:#6b6b6b;
  --topbar:#efefef;
  --events:#464646;
  --footer:#1c1c1c;
  --line:#d9d9d9;
  --white:#fff;
}
*{margin:0;padding:0;box-sizing:border-box}
html,body{width:1200px;height:2894px;overflow:hidden;background:var(--white)}
body{position:relative;font-family:'Poppins',sans-serif;color:var(--ink)}
.abs{position:absolute}
.topbar{top:0;left:0;width:1200px;height:38px;background:var(--topbar);display:flex;justify-content:center;align-items:center;gap:6px}
.social-dot{width:18px;height:18px;border:1.5px solid #333;border-radius:50%}
.header{top:38px;left:0;width:1200px;height:62px}
.logo{font-family:'Poppins',sans-serif;font-weight:500;font-size:30px;color:var(--teal);letter-spacing:1px}
.header .logo{left:96px;top:12px}
.call{left:930px;top:8px;display:flex;align-items:center;gap:14px}
.call-icon{width:32px;height:32px;border:2px solid var(--teal);border-radius:50%;display:flex;align-items:center;justify-content:center}
.call-label{font-size:13px;color:#444}
.call-number{font-family:'Roboto',sans-serif;font-size:19px;font-weight:500;color:#222;letter-spacing:.5px}
.nav{top:100px;left:0;width:1200px;height:34px;background:var(--teal);display:flex;align-items:center;font-family:'Roboto',sans-serif;font-size:13.5px;color:var(--white)}
.nav span{position:absolute;top:9px}
.hero{top:134px;left:0;width:1200px;height:454px;background:linear-gradient(180deg,#5d5d5d 0%,#4a4a4a 45%,#6e6a66 100%)}
.hero-title{top:196px;left:0;width:1200px;text-align:center;font-family:'Bree Serif',serif;font-size:33px;line-height:58px;color:var(--white)}
.intro-heading{left:118px;top:636px;width:460px;font-family:'Bree Serif',serif;font-size:25px;line-height:44px;color:#222}
.para{font-size:10.5px;line-height:23px;color:var(--body)}
.intro-text{left:118px;top:738px;width:440px}
.btn{left:118px;top:878px;width:166px;height:42px;background:var(--teal);border-radius:3px;color:var(--white);font-family:'Roboto',sans-serif;font-size:16px;font-weight:500;display:flex;align-items:center;justify-content:center}
.photo{border-radius:4px}
.section-title{font-family:'Bree Serif',serif;font-size:25px;color:#222}
.rule{height:1px;background:var(--line)}
.card-title{font-family:'Bree Serif',serif;font-size:15px;color:#222}
.card-text{font-size:10px;line-height:23px;color:#888;width:312px;text-align:justify}
.more{color:#222;text-decoration:underline}
.events{top:1491px;left:0;width:1200px;height:382px;background:var(--events)}
.date{width:77px;height:66px;background:var(--teal);color:var(--white);font-family:'Roboto',sans-serif;text-align:center;padding-top:8px}
.date b{display:block;font-size:24px;font-weight:500;line-height:26px}
.date i{font-style:normal;font-size:16px}
.event-title{font-family:'Roboto',sans-serif;font-weight:500;font-size:13px;color:var(--white)}
.event-text{font-size:10.5px;line-height:22px;color:#ededed;width:290px}
.contact{top:2533px;left:127px;width:946px;height:110px;background:var(--teal)}
.contact-line{font-family:'Roboto',sans-serif;font-weight:500;font-size:19px;color:var(--white)}
.contact-sub{font-family:'Roboto',sans-serif;font-size:14.5px;color:var(--white)}
.touch{left:641px;top:27px;width:266px;height:50px;border:2px solid var(--white);border-radius:6px;display:flex;align-items:center;justify-content:center;font-family:'Roboto',sans-serif;font-size:23px;color:var(--white)}
.footer{top:2678px;left:0;width:1200px;height:216px;background:var(--footer)}
.footer-link{font-family:'Roboto',sans-serif;font-size:13.5px;line-height:27px;color:#ddd}
.ring{width:25px;height:25px;border:1.5px solid #ddd;border-radius:50%;display:inline-block;margin-right:6px}
</style>
</head>
<body>

<div class="abs topbar">
  <span class="social-dot"></span><span class="social-dot"></span><span class="social-dot"></span><span class="social-dot"></span>
</div>

<header class="abs header">
  <div class="abs logo">Ardo Move</div>
  <div class="abs call">
    <div class="call-icon"><svg width="16" height="16" viewBox="0 0 24 24"><path d="M6.6 10.8a15 15 0 0 0 6.6 6.6l2.2-2.2a1 1 0 0 1 1-.25 11.4 11.4 0 0 0 3.6.57 1 1 0 0 1 1 1V20a1 1 0 0 1-1 1A17 17 0 0 1 3 4a1 1 0 0 1 1-1h3.5a1 1 0 0 1 1 1c0 1.25.2 2.45.57 3.57a1 1 0 0 1-.25 1z" fill="#14b99b"/></svg></div>
    <div><div class="call-label">Call Us Today</div><div class="call-number">1800 555 014</div></div>
  </div>
</header>

<nav class="abs nav">
  <span style="left:62px">Home</span>
  <span style="left:175px">About us</span>
  <span style="left:306px">Trips</span>
  <span style="left:418px">Trainers/ Hosts</span>
  <span style="left:594px">Register</span>
  <span style="left:718px">Albums</span>
  <span style="left:843px">Donate</span>
  <span style="left:966px">FAQ</span>
  <span style="left:1071px">Contact us</span>
</nav>

<section class="abs hero" role="img" aria-label="Children playing in a circle between tents at a refugee camp"></section>
<h1 class="abs hero-title">Take Care Of Your Body. It’s The Only Place<br>You Have To Live</h1>

<section>
  <h2 class="abs intro-heading">Neque porro quisquam est qui dolorem ipsum quia dolor sit amet,</h2>
  <p class="abs para intro-text">Lorem Ipsum is simply dummy text of the printing and typesetting industry. Lorem Ipsum has been the industry's standard dummy text ever since the 1500s, when an unknown printer took a galley of type and scrambled it to make Lorem Ipsum is simply dummy text of the printing and typesetting industry. Lorem Ipsum has been the industry's standard dummy text ever since the 1500s.</p>
  <div class="abs btn">Donate Today</div>
  <div class="abs" role="img" aria-label="Volunteer beside a tent on a rocky mountain slope" style="left:602px;top:635px;width:482px;height:297px;background:linear-gradient(160deg,#8f9a86 0%,#6f7a6a 50%,#9a9890 100%)"></div>
</section>

<section>
  <h2 class="abs section-title" style="left:118px;top:1004px">Our Causes</h2>
  <div class="abs rule" style="left:118px;top:1044px;width:984px"></div>

  <div class="abs photo" role="img" aria-label="Child riding on a man's shoulders in a crowd" style="left:118px;top:1078px;width:312px;height:234px;background:linear-gradient(180deg,#8fa3b5 0%,#5a5f66 60%,#2f3135 100%)"></div>
  <h3 class="abs card-title" style="left:118px;top:1326px">Reaching Remote Regions</h3>
  <p class="abs card-text" style="left:118px;top:1360px">Lorem Ipsum is simply dummy text of the printing and typesetting industry. Lorem Ipsum has been the indu stry's standard dummy <span class="more">Read More...</span></p>

  <div class="abs photo" role="img" aria-label="Crowded rubber boat of people at sea" style="left:453px;top:1078px;width:312px;height:234px;background:linear-gradient(180deg,#6d7780 0%,#3c3f45 55%,#5d6670 100%)"></div>
  <h3 class="abs card-title" style="left:453px;top:1326px">A Target Of 2000 Children</h3>
  <p class="abs card-text" style="left:453px;top:1360px">Lorem Ipsum is simply dummy text of the printing and typesetting industry. Lorem Ipsum has been the indu stry's standard dummyLorem Ipsum. <span class="more">Read More...</span></p>

  <div class="abs photo" role="img" aria-label="Child peeking out from a tarpaulin shelter" style="left:787px;top:1078px;width:312px;height:234px;background:linear-gradient(180deg,#c9c8c6 0%,#a9a7a3 50%,#d6d3cf 100%)"></div>
  <h3 class="abs card-title" style="left:787px;top:1326px">Help Us Raise Funds</h3>
  <p class="abs card-text" style="left:787px;top:1360px">Lorem Ipsum is simply dummy text of the printing and typesetting industry. Lorem Ipsum has been the indu stry's standard dummyLorem Ipsum. <span class="more">Read More...</span></p>
</section>

<section class="abs events">
  <h2 class="abs section-title" style="left:0;width:1200px;text-align:center;top:39px;color:#fff">Our Events</h2>
  <div class="abs rule" style="left:118px;top:89px;width:984px;background:#8a8a8a"></div>

  <div class="abs date" style="left:183px;top:141px"><b>06</b><i>Aug</i></div>
  <div class="abs event-title" style="left:283px;top:142px">Neque porro quisquam est qui dolorem</div>
  <p class="abs event-text" style="left:283px;top:170px">Lorem Ipsum is simply dummy text of the printing and typesetting industry. Lorem Ipsum</p>

  <div class="abs date" style="left:633px;top:141px"><b>05</b><i>Aug</i></div>
  <div class="abs event-title" style="left:736px;top:137px">Neque porro quisquam est qui dolorem</div>
  <p class="abs event-text" style="left:736px;top:165px">Lorem Ipsum is simply dummy text of the printing and typesetting industry. Lorem Ipsum</p>

  <div class="abs date" style="left:183px;top:259px"><b>03</b><i>Aug</i></div>
  <div class="abs event-title" style="left:283px;top:260px">Neque porro quisquam est qui dolorem</div>
  <p class="abs event-text" style="left:283px;top:288px">Lorem Ipsum is simply dummy text of the printing and typesetting industry. Lorem Ipsum</p>

  <div class="abs date" style="left:633px;top:259px"><b>02</b><i>Aug</i></div>
  <div class="abs event-title" style="left:736px;top:255px">Neque porro quisquam est qui dolorem</div>
  <p class="abs event-text" style="left:736px;top:283px">Lorem Ipsum is simply dummy text of the printing and typesetting industry. Lorem Ipsum</p>
</section>

<section>
  <h2 class="abs section-title" style="left:0;width:1200px;text-align:center;top:1918px;font-size:29px;color:#333">Check Out Our Blog</h2>
  <p class="abs para" style="left:180px;top:1976px;width:840px;text-align:center;font-size:10px;color:#888">Lorem Ipsum is simply dummy text of the printing and typesetting industry. Lorem Ipsum has been the industry's standard dummy text ever since the 1500s, when an unknown printer took a galley of type and scrambled it to make a type specimen book.Lorem Ipsum</p>

  <div class="abs photo" role="img" aria-label="Silhouettes of a woman and child behind a wire fence" style="left:98px;top:2049px;width:485px;height:301px;background:linear-gradient(180deg,#c1bbb4 0%,#8d857d 55%,#3a3633 100%)"></div>
  <h3 class="abs" style="left:98px;top:2378px;font-family:'Roboto',sans-serif;font-weight:500;font-size:14.5px;color:#222">Lorem Ipsum is simply dummy text of the printing and typesetting</h3>
  <p class="abs card-text" style="left:98px;top:2416px;width:485px">Lorem Ipsum is simply dummy text of the printing and typesetting industry. Lorem Ipsum has been the industry's standard dummy text ever since the 1500s, when an unknown printer took a galley of type and scrambled it to make a type specimen book. <span class="more">Read More...</span></p>

  <div class="abs photo" role="img" aria-label="Tents at a camp with a child seated in front" style="left:615px;top:2049px;width:485px;height:301px;background:linear-gradient(180deg,#6f86a6 0%,#8a8f86 45%,#5f6a55 100%)"></div>
  <h3 class="abs" style="left:615px;top:2378px;font-family:'Roboto',sans-serif;font-weight:500;font-size:14.5px;color:#222">Lorem Ipsum is simply dummy text of the printing and typesetting</h3>
  <p class="abs card-text" style="left:615px;top:2416px;width:485px">Lorem Ipsum is simply dummy text of the printing and typesetting industry. Lorem Ipsum has been the industry's standard dummy text ever since the 1500s, when an unknown printer took a galley of type and scrambled it to make a type specimen book. <span class="more">Read More...</span></p>
</section>

<section class="abs contact">
  <div class="abs" style="left:38px;top:26px;width:58px;height:58px;border:2.5px solid #fff;border-radius:50%;display:flex;align-items:center;justify-content:center">
    <svg width="28" height="28" viewBox="0 0 24 24"><path d="M6.6 10.8a15 15 0 0 0 6.6 6.6l2.2-2.2a1 1 0 0 1 1-.25 11.4 11.4 0 0 0 3.6.57 1 1 0 0 1 1 1V20a1 1 0 0 1-1 1A17 17 0 0 1 3 4a1 1 0 0 1 1-1h3.5a1 1 0 0 1 1 1c0 1.25.2 2.45.57 3.57a1 1 0 0 1-.25 1z" fill="#fff"/></svg>
  </div>
  <div class="abs contact-line" style="left:133px;top:27px">Contact US Now ! &nbsp;&nbsp;555 0190 2231</div>
  <div class="abs contact-sub" style="left:133px;top:62px">Neque porro quisquam est qui dolorem ipsum quia dolorem ipsum quia</div>
  <div class="abs touch">Get In Touch</div>
</section>

<footer class="abs footer">
  <div class="abs logo" style="left:145px;top:48px;font-size:32px">Ardo Move</div>
  <div class="abs" style="left:168px;top:104px"><span class="ring"></span><span class="ring"></span><span class="ring"></span><span class="ring"></span></div>
  <div class="abs footer-link" style="left:434px;top:37px">About Us<br>Programs<br>Get &nbsp;involved<br>Projects</div>
  <div class="abs footer-link" style="left:618px;top:37px">Blog<br>Privacy Policy<br>Contacts<br>Terms of use</div>
  <div class="abs" style="left:803px;top:40px;font-family:'Roboto',sans-serif;font-size:17px;color:#eee">Newsletter</div>
  <div class="abs" style="left:801px;top:77px;width:183px;height:31px;background:#333;color:#bbb;font-size:9px;padding:9px 14px">Enter your email</div>
  <div class="abs" style="left:984px;top:77px;width:116px;height:31px;background:var(--teal);color:#fff;font-family:'Roboto',sans-serif;font-weight:500;font-size:10.5px;display:flex;align-items:center;justify-content:center">SUBSCRIBE</div>
  <div class="abs rule" style="left:98px;top:175px;width:1002px;background:#333"></div>
  <div class="abs" style="left:0;width:1200px;top:187px;text-align:center;font-size:9.5px;font-weight:500;color:#ddd">© 2017 Ardo Move. Terms and Conditions Privacy Policy</div>
</footer>

</body>
</html>
```